Fresh and unique Mortgage Broking business needs website design.

We need a professional yet fresh, bright and colourful website for my Mortgage broking business.
We specialise in the Non conforming/sub prime market with clients who have been rejected by other banks or have trouble getting finance through a traditional lender.
We are called Brightwell Lending and we aim to provide Hope to our clients when they have thought there was no hope.
I would like it to be on a Wordpress platform as I plan to do a lot of postings, both written and video and I need it to be easy to use.
I would also like it to be able to have a clear and simple enquiry box on the first page to capture contact details and notify me via email.

I have already had the logo designed in both green and black and a white version.
I have also had a a header made up using the white logo with leaves background that could possibly be used as the website header which I have used as my facebook header.

https://www.facebook.com/MarcusTolvenBright/

I tried playing around with a jimdo website builder which kind of got some of the brightness and colours I was after but it had a lot to go.

http://brightwelllending.sitevale.example/

Industry/Entity Type

Finance

Number of Pages Required

4 page

Colors
0292cd
00a990
fbed22
ffc214
f78f20
ec1f27

Requirements
Nice to have
• I'm not sure what the difference between uncoded and coded website is so I'm not sure what I need?

```html
<!DOCTYPE html>
<html lang="en">
<head>
<meta charset="utf-8">
<title>Brightwell Lending</title>
<link href="https://fonts.googleapis.com/css2?family=Lato:wght@400;700&family=Libre+Baskerville:wght@700&display=swap" rel="stylesheet">
<style>
:root{
  --green:#176b35;
  --green-dark:#0f5229;
  --ink:#161616;
  --text:#2b2b2b;
  --muted:#6f6f6f;
  --grey-band:#efefef;
  --rule:#c9c9c9;
  --footer:#333333;
  --footer-rule:#4a4a4a;
  --white:#ffffff;
}
*{margin:0;padding:0;box-sizing:border-box}
html,body{width:1200px;height:2413px;overflow:hidden}
body{position:relative;font-family:"Lato",Arial,sans-serif;color:var(--text);background:var(--white)}
.abs{position:absolute}
.serif{font-family:"Libre Baskerville",Georgia,serif;font-weight:700}
.green{color:var(--green)}

/* hero */
.hero{left:0;top:0;width:1200px;height:640px;background:
  radial-gradient(ellipse 420px 320px at 300px 330px,#9fae6a 0%,rgba(159,174,106,0) 70%),
  radial-gradient(ellipse 500px 380px at 1000px 160px,#fbf3dc 0%,rgba(251,243,220,0) 75%),
  linear-gradient(90deg,#6e7f48 0%,#c9c08a 45%,#f1e6c6 75%,#efe2c0 100%)}
.hero-ground{left:0;top:520px;width:1200px;height:120px;background:linear-gradient(180deg,rgba(188,160,120,0) 0%,#b99c76 60%,#a8855d 100%)}
.brand{left:158px;top:60px;display:flex;align-items:center;gap:10px}
.brand-dot{width:18px;height:18px;border-radius:50%;background:var(--green)}
.brand-name{font-size:34px;font-weight:700;color:var(--green);line-height:1}
.top-contact{top:28px;font-size:12px;line-height:16px;color:var(--ink);display:flex;gap:8px;align-items:center}
.top-contact b{color:var(--green);font-size:11px;display:block}
.nav{left:468px;top:85px;display:flex;align-items:center;font-family:"Libre Baskerville",Georgia,serif;font-weight:700;font-size:14px;color:var(--green);letter-spacing:.3px}
.nav a{color:inherit;text-decoration:none;margin-right:36px}
.nav a.active{background:var(--green);color:var(--white);padding:8px 11px;margin-right:20px}
.nav a:last-child{margin-right:0}
.headline{right:164px;top:300px;text-align:right;font-size:39px;line-height:52px;color:var(--ink)}
.dots{left:968px;top:480px;display:flex;gap:11px}
.dots span{width:12px;height:12px;border-radius:50%;background:var(--ink)}
.dots span.on{background:var(--green)}

/* section titles */
.title{font-size:28px;color:var(--ink);letter-spacing:.3px}
.rule{height:1px;background:var(--rule)}
.rule::before{content:"";display:block;width:95px;height:3px;background:var(--green);margin-top:-1px}
.rule.center::before{margin-left:auto;margin-right:auto}

/* about */
.about-text{left:158px;top:746px;width:275px;font-size:14px;line-height:25px;color:var(--text)}
.about-text a{color:var(--green);text-decoration:none}
.vsep{left:466px;top:690px;width:1px;height:280px;background:linear-gradient(180deg,rgba(0,0,0,0),#d8d8d8 30%,#d8d8d8 70%,rgba(0,0,0,0))}
.dove-art{left:499px;top:756px;width:186px;height:174px;border-radius:8px;background:radial-gradient(circle at 50% 50%,#e9eee9 0%,#f7f9f7 80%)}
.service{display:flex;align-items:center;gap:10px;font-size:13px;color:var(--ink)}
.icon-dot{width:34px;height:34px;border-radius:50%;background:var(--green);display:flex;align-items:center;justify-content:center;flex:none}

/* why */
.why{left:0;top:999px;width:1200px;height:433px;background:var(--grey-band)}
.feature-icon{width:84px;height:84px;border-radius:50%;border:2px solid var(--green);background:var(--white);display:flex;align-items:center;justify-content:center}
.feature h3{font-size:18px;font-weight:700;color:var(--ink);margin-bottom:6px}
.feature p{font-size:11.5px;line-height:16px;color:var(--text)}
.feature p b{color:var(--green)}
.feature.left{text-align:right}

/* quote */
.quote{left:0;top:1432px;width:1200px;height:394px;background:
  radial-gradient(ellipse 420px 260px at 900px 250px,rgba(140,70,40,.45) 0%,rgba(0,0,0,0) 70%),
  radial-gradient(ellipse 300px 300px at 160px 160px,rgba(90,110,120,.35) 0%,rgba(0,0,0,0) 70%),
  linear-gradient(180deg,#2a2f33 0%,#1d2326 100%)}
.field{background:rgba(200,200,200,.55);color:var(--white);font-size:12px;padding:6px 10px;border-radius:2px}
.btn{background:var(--green);color:var(--white);font-weight:700;font-size:15px;text-align:center;letter-spacing:.3px}

/* clients */
.client{top:1969px;width:161px;height:69px;border:1px solid #dcdcdc;display:flex;align-items:center;justify-content:center;gap:8px;font-size:22px;font-weight:700;color:#4a4a4a}
.client i{width:14px;height:14px;border-radius:50%;background:#4a4a4a}

/* footer */
.footer{left:0;top:2091px;width:1200px;height:275px;background:var(--footer);color:#e6e6e6}
.fhead{font-size:14px;font-weight:700;color:var(--white)}
.fhead span{color:var(--green)}
.frule{height:1px;background:var(--footer-rule)}
.flinks{list-style:none;font-size:12px;line-height:31px;color:#e6e6e6}
.flinks li::before{content:"›";color:var(--green);margin-right:8px}
.fvsep{top:2130px;width:1px;height:200px;background:var(--footer-rule)}
.fcontact{font-size:12px;line-height:18px}
.fline{display:flex;align-items:center;gap:10px;font-size:12px}
.bar{left:0;top:2366px;width:1200px;height:47px;background:var(--green)}
.social{width:28px;height:28px;border-radius:50%;border:2px solid var(--white)}
</style>
</head>
<body>

<!-- hero -->
<div class="abs hero" role="img" aria-label="Photo of a glass jar of coins with a green seedling growing from it, soft bokeh background"></div>
<div class="abs hero-ground" role="img" aria-label="Wooden table surface under the coin jar"></div>

<div class="abs brand"><span class="brand-dot"></span><span class="brand-name">Brightwell Lending</span></div>

<div class="abs top-contact" style="left:732px">
  <svg width="26" height="20" viewBox="0 0 26 20"><path d="M5 3c2 0 3 3 2 4l-1 1c1 2 3 4 5 5l1-1c1-1 4 0 4 2l-1 2c-6 1-12-5-12-11z" fill="none" stroke="#161616" stroke-width="1.4"/></svg>
  <div><b>Phone</b>123 456 7890</div>
</div>
<div class="abs top-contact" style="left:868px">
  <svg width="26" height="20" viewBox="0 0 26 20"><rect x="3" y="4" width="18" height="12" fill="none" stroke="#161616" stroke-width="1.4"/><path d="M3 4l9 7 9-7" fill="none" stroke="#161616" stroke-width="1.4"/></svg>
  <div><b>Email</b>inquiry@brightwelllending.example</div>
</div>

<nav class="abs nav">
  <a class="active" href="#">HOME</a>
  <a href="#">ABOUT US</a>
  <a href="#">OUR SERVICES</a>
  <a href="#">PROPERTY ADVICE</a>
  <a href="#">CONTACT</a>
</nav>

<h1 class="abs headline serif">HOPE FOR YOUR<br>FINANCE WHEN<br><span class="green">ALL HOPE IS LOST</span></h1>
<div class="abs dots"><span></span><span class="on"></span><span></span></div>

<!-- about -->
<h2 class="abs title serif" style="left:158px;top:680px">ABOUT <span class="green">US</span></h2>
<div class="abs rule" style="left:158px;top:724px;width:281px"></div>
<p class="abs about-text">Lorem ipsum dolor sit amet, consectetuer ing elit, sed diam nonummy nibh euismod icidunt errt laoreet dolore magna aliquam erat utpati Ut ieer enim ad minim veniam, quis nostrudw tionweri ullamcorpererer suscipit lobortis isl ut aliquip exir commodo consequat. Duis tem vel eu. Lorem ium dolor sit amet errer itetuer ewrerer &nbsp;tation ullamc... &nbsp;<a href="#">READ MORE+</a></p>
<div class="abs vsep"></div>

<!-- services -->
<h2 class="abs title serif" style="left:495px;top:680px">OUR <span class="green">SERVICES</span></h2>
<div class="abs rule" style="left:495px;top:724px;width:283px"></div>
<div class="abs dove-art" role="img" aria-label="Line illustration of a dove carrying an olive branch"></div>

<div class="abs service" style="left:745px;top:760px"><span class="icon-dot"><svg width="18" height="18" viewBox="0 0 18 18"><rect x="2" y="4" width="14" height="10" rx="1" fill="none" stroke="#fff" stroke-width="1.6"/><path d="M2 8h14" stroke="#fff" stroke-width="1.6"/></svg></span>Bad Credit</div>
<div class="abs service" style="left:919px;top:781px"><span class="icon-dot"><svg width="18" height="18" viewBox="0 0 18 18"><rect x="4" y="2" width="10" height="14" fill="none" stroke="#fff" stroke-width="1.6"/><path d="M6 6h6M6 9h6M6 12h4" stroke="#fff" stroke-width="1.4"/></svg></span>Low Doc</div>
<div class="abs service" style="left:707px;top:810px"><span class="icon-dot"><svg width="18" height="18" viewBox="0 0 18 18"><circle cx="9" cy="9" r="6" fill="none" stroke="#fff" stroke-width="1.6"/><path d="M9 5v8M7 7h3a1.5 1.5 0 010 3H8a1.5 1.5 0 000 3h3" fill="none" stroke="#fff" stroke-width="1.3"/></svg></span>Investment Loans</div>
<div class="abs service" style="left:882px;top:836px"><span class="icon-dot"><svg width="18" height="18" viewBox="0 0 18 18"><path d="M3 9l6-5 6 5v6H3z" fill="none" stroke="#fff" stroke-width="1.6"/><rect x="7.5" y="11" width="3" height="4" fill="#fff"/></svg></span>Residential Loans</div>
<div class="abs service" style="left:667px;top:860px"><span class="icon-dot"><svg width="18" height="18" viewBox="0 0 18 18"><rect x="3" y="3" width="10" height="12" fill="none" stroke="#fff" stroke-width="1.6"/><path d="M8 12l7-7" stroke="#fff" stroke-width="1.8"/></svg></span>Self Employed Loans</div>
<div class="abs service" style="left:845px;top:893px"><span class="icon-dot"><svg width="18" height="18" viewBox="0 0 18 18"><path d="M15 9a6 6 0 11-2-4.5" fill="none" stroke="#fff" stroke-width="1.6"/><path d="M13 2v3h-3" fill="none" stroke="#fff" stroke-width="1.6"/><path d="M9 6v6" stroke="#fff" stroke-width="1.4"/></svg></span>Debt Consolidation</div>
<div class="abs service" style="left:628px;top:911px"><span class="icon-dot"><svg width="18" height="18" viewBox="0 0 18 18"><rect x="2" y="5" width="14" height="10" rx="1" fill="none" stroke="#fff" stroke-width="1.6"/><path d="M6 5V3h6v2M2 9h14" fill="none" stroke="#fff" stroke-width="1.4"/></svg></span>Non Confirming Loans</div>

<!-- why choose us -->
<div class="abs why"></div>
<h2 class="abs title serif" style="left:0;width:1200px;top:1040px;text-align:center">WHY <span class="green">CHOOSE US</span></h2>
<div class="abs rule center" style="left:457px;top:1089px;width:283px"></div>

<div class="abs feature left" style="left:170px;top:1146px;width:279px">
  <h3>Satisfied Clients</h3>
  <p>Lorem ipsum dolor sit amet, consectetuer ing elit werewr dolore magna aliquam erat utpati ... <b>[+]</b></p>
</div>
<div class="abs feature-icon" style="left:487px;top:1137px"><svg width="44" height="44" viewBox="0 0 44 44"><circle cx="18" cy="18" r="7" fill="#1f1f1f"/><path d="M6 38c0-8 5-12 12-12s12 4 12 12z" fill="#1f1f1f"/><rect x="24" y="5" width="16" height="11" rx="2" fill="#176b35"/><circle cx="28" cy="10.5" r="1.2" fill="#fff"/><circle cx="32" cy="10.5" r="1.2" fill="#fff"/><circle cx="36" cy="10.5" r="1.2" fill="#fff"/></svg></div>
<div class="abs feature-icon" style="left:624px;top:1137px"><svg width="44" height="44" viewBox="0 0 44 44"><rect x="7" y="9" width="30" height="28" rx="3" fill="none" stroke="#1f1f1f" stroke-width="3"/><path d="M14 5v8M30 5v8" stroke="#1f1f1f" stroke-width="3"/><path d="M37 28l-9 9" stroke="#176b35" stroke-width="3"/></svg></div>
<div class="abs feature" style="left:730px;top:1146px;width:280px">
  <h3>Fast Work and Help</h3>
  <p>Lorem ipsum dolor sit amet, consectetuer ing elit werewr dolore magna aliquam erat utpati ... <b>[+]</b></p>
</div>

<div class="abs feature left" style="left:170px;top:1302px;width:279px">
  <h3>Year of Experience</h3>
  <p>Lorem ipsum dolor sit amet, consectetuer ing elit werewr dolore magna aliquam erat utpati ... <b>[+]</b></p>
</div>
<div class="abs feature-icon" style="left:487px;top:1285px"><svg width="44" height="44" viewBox="0 0 44 44"><circle cx="22" cy="17" r="11" fill="#1f1f1f"/><circle cx="22" cy="17" r="6" fill="#fff"/><path d="M15 26l-4 14 6-3 3 5 2-14zM29 26l4 14-6-3-3 5-2-14z" fill="#176b35"/></svg></div>
<div class="abs feature-icon" style="left:624px;top:1285px"><svg width="44" height="44" viewBox="0 0 44 44"><rect x="4" y="9" width="34" height="24" fill="none" stroke="#1f1f1f" stroke-width="3"/><path d="M10 17h14M10 23h10" stroke="#1f1f1f" stroke-width="2.5"/><circle cx="32" cy="27" r="6" fill="#176b35"/><path d="M29 32l-1 7 4-2 4 2-1-7" fill="#176b35"/></svg></div>
<div class="abs feature" style="left:730px;top:1302px;width:280px">
  <h3>Certified Experts</h3>
  <p>Lorem ipsum dolor sit amet, consectetuer ing elit werewr dolore magna aliquam erat utpati ... <b>[+]</b></p>
</div>

<!-- request a quote -->
<div class="abs quote" role="img" aria-label="Dark background photo of financial line charts and data grid"></div>
<h2 class="abs title serif" style="left:0;width:1200px;top:1478px;text-align:center;color:#fff">REQUEST A QUOTE</h2>
<div class="abs" style="left:457px;top:1530px;width:283px;height:1px;background:rgba(255,255,255,.45)"></div>
<div class="abs field" style="left:251px;top:1554px;width:343px;height:31px">Name*</div>
<div class="abs field" style="left:605px;top:1554px;width:343px;height:31px">Email*</div>
<div class="abs field" style="left:251px;top:1596px;width:343px;height:29px">Phone*</div>
<div class="abs field" style="left:605px;top:1596px;width:343px;height:29px">Company</div>
<div class="abs field" style="left:251px;top:1638px;width:697px;height:74px">Messages</div>
<div class="abs btn" style="left:513px;top:1736px;width:169px;height:35px;line-height:35px">SUBMIT A QUOTE</div>

<!-- clients -->
<h2 class="abs title serif" style="left:0;width:1200px;top:1872px;text-align:center">OUR <span class="green">CLIENTS</span></h2>
<div class="abs rule center" style="left:457px;top:1922px;width:283px"></div>
<div class="abs client" style="left:156px">Northvale</div>
<div class="abs client" style="left:336px"><i></i>Corvane</div>
<div class="abs client" style="left:516px"><i></i>Meridex</div>
<div class="abs client" style="left:697px"><i></i>Halbrook</div>
<div class="abs client" style="left:877px;color:#9a9a9a">Tessan</div>

<!-- footer -->
<div class="abs footer"></div>
<div class="abs fhead" style="left:158px;top:2130px">QUICK <span>LINKS</span></div>
<div class="abs frule" style="left:158px;top:2156px;width:120px"></div>
<ul class="abs flinks" style="left:163px;top:2164px">
  <li>HOME</li><li>ABOUT US</li><li>OUR SERVICES</li><li>PROPERTY ADVICE</li><li>CONTACT US</li>
</ul>
<div class="abs fvsep" style="left:298px"></div>

<div class="abs fhead" style="left:327px;top:2130px">CONTACT <span>DETAIL</span></div>
<div class="abs frule" style="left:327px;top:2156px;width:195px"></div>
<div class="abs fcontact" style="left:327px;top:2170px"><b>BRIGHTWELL LENDING</b><br>123, Ut wisi enim ad minim veniam,<br>Mor nostrni tation -123 456</div>
<div class="abs fline" style="left:327px;top:2237px"><svg width="12" height="12" viewBox="0 0 12 12"><path d="M2 1c1 0 2 2 1 3l-.5.5c.7 1.4 2 2.7 3.4 3.4L6.5 7.4c1-1 3 0 3 1L9 10C5 10.6 1.4 7 2 1z" fill="#176b35"/></svg>(123) 456 7890</div>
<div class="abs fline" style="left:327px;top:2266px"><svg width="12" height="12" viewBox="0 0 12 12"><rect x="1" y="3" width="10" height="7" fill="none" stroke="#176b35" stroke-width="1.4"/><path d="M3 3V1h6v2" fill="none" stroke="#176b35" stroke-width="1.4"/></svg>(123) 456 7890</div>
<div class="abs fline" style="left:327px;top:2296px"><svg width="12" height="12" viewBox="0 0 12 12"><rect x="1" y="2.5" width="10" height="7" fill="none" stroke="#176b35" stroke-width="1.3"/><path d="M1 2.5l5 4 5-4" fill="none" stroke="#176b35" stroke-width="1.3"/></svg>inquiry@brightwelllending.example</div>
<div class="abs fvsep" style="left:539px"></div>

<div class="abs fhead" style="left:565px;top:2130px">NEWSLETTER <span>SIGN UP</span></div>
<div class="abs frule" style="left:565px;top:2156px;width:226px"></div>
<p class="abs" style="left:565px;top:2174px;width:240px;font-size:11.5px;line-height:17px">Lorem Ipsum Dolor Sit Amet, Consectetuer Adipiscing Elit &nbsp;Sed Diam Nonummy Nibh</p>
<div class="abs" style="left:565px;top:2220px;width:226px;height:29px;background:#fff;color:#222;font-size:11px;padding:8px 10px">Email</div>
<div class="abs btn" style="left:565px;top:2260px;width:93px;height:27px;line-height:27px;font-size:13px">SUBMIT</div>
<div class="abs fvsep" style="left:820px"></div>

<div class="abs" style="left:842px;top:2196px;display:flex;align-items:center;gap:8px">
  <span style="width:14px;height:14px;border-radius:50%;background:#fff"></span>
  <span style="font-size:24px;font-weight:700;color:#fff">Brightwell Lending</span>
</div>

<div class="abs bar"></div>
<p class="abs" style="left:161px;top:2382px;font-size:12px;color:#fff">Copyright © 2016 Brightwell Lending. All Rights Reserved.</p>
<div class="abs social" style="left:898px;top:2375px" aria-label="Social link one"></div>
<div class="abs social" style="left:935px;top:2375px" aria-label="Social link two"></div>
<div class="abs social" style="left:972px;top:2375px" aria-label="Social link three"></div>
<div class="abs social" style="left:1009px;top:2375px" aria-label="Social link four"></div>

</body>
</html>
```